Wine Label for White and Red Wine from California

We need a wine label for 2 whites and 2 red wines. (Merlot, Cabernet Sauvignon, Chardonnay, Pinot Grigio) Can be the same label or can have something to differentiate among them such as a color change. This is a label for an already existing wine on the US market but needs to be completely re-done. We want something way sharper, eye catching. Don't use the original label please as your starting point-- I don't think we want to see it anymore. But the structure of it is ok and the fonts are ok. (The tree is what is so awful about)

Target Market(s)

US market, always good to think of millennials, but still appeal to all ages. Men and women.

Colors

Designer to choose colors to be used in the design.

Requirements
Must have
• Should be eye catching, grabs attention, looks expensive, sells for a value price. Should feature the brand name and varietal and vintage:
• Dorvane Vineyards / Cabernet Sauvignon / 2014
• Bottle type is the 'Bordeaux Style' bottle. The white wine is a green bottle, the red wine uses a dark brown bottle. Be sure the labels look good on these bottles.
• What this bottle looks like is shown below.
• The label we are replacing is shown in the briefs.
Nice to have
• We feel successful labels have a lot of white background, stay away from dark labels-- they scratch too much when handled.
• Attached is a label we like, please look at the Cadenza label image below. But at the same time, we are flexible to your creativity. But nothing too crazy please.
Should not have
• Should not have a dark background.
• We are not big fans of grapes on the label unless extremely stylised. Nor do we like wine glasses, wine bottles.

```html
<!DOCTYPE html>
<html lang="en">
<head>
<meta charset="utf-8">
<title>Dorvane Vineyards — Pinot Grigio Label</title>
<link rel="stylesheet" href="https://fonts.googleapis.com/css2?family=Cormorant+Garamond:wght@500;600&display=swap">
<style>
  :root {
    --page: #ffffff;
    --paper: #ffffff;
    --ink: #111111;
    --band: #0b0b0b;
    --band-text: #ffffff;
    --wash-light: #efe6cf;
    --wash-sand: #d9c89a;
    --wash-olive: #a9a66a;
    --wash-moss: #6f7446;
    --wash-dark: #1d1c17;
  }
  * { margin: 0; padding: 0; box-sizing: border-box; }
  html, body {
    width: 1200px;
    height: 1155px;
    overflow: hidden;
    background: var(--page);
  }
  .canvas {
    position: relative;
    width: 1200px;
    height: 1155px;
  }
  .label {
    position: absolute;
    left: 240px;
    top: 67px;
    width: 720px;
    height: 1020px;
    background: var(--paper);
    box-shadow: 6px 8px 14px rgba(0, 0, 0, 0.28);
    font-family: "Cormorant Garamond", Georgia, serif;
    color: var(--ink);
    overflow: hidden;
  }
  .brand {
    position: absolute;
    top: 10px;
    left: 0;
    width: 100%;
    text-align: center;
  }
  .brand-name {
    display: block;
    font-size: 104px;
    font-weight: 500;
    line-height: 1.1;
    letter-spacing: 0.13em;
    margin-right: -0.13em;
  }
  .brand-sub {
    display: block;
    margin-top: 14px;
    font-size: 44px;
    font-weight: 500;
    line-height: 1;
    letter-spacing: 0.46em;
    margin-right: -0.46em;
  }
  .landscape {
    position: absolute;
    left: 0;
    top: 400px;
    width: 100%;
    height: 340px;
  }
  .varietal {
    position: absolute;
    top: 898px;
    left: 0;
    width: 100%;
    text-align: center;
    font-size: 40px;
    font-weight: 500;
    letter-spacing: 0.03em;
    line-height: 1;
  }
  .vintage-band {
    position: absolute;
    left: 0;
    bottom: 0;
    width: 100%;
    height: 70px;
    background: var(--band);
    color: var(--band-text);
    display: flex;
    align-items: center;
    justify-content: center;
    font-size: 38px;
    font-weight: 500;
    letter-spacing: 0.04em;
    font-variant-numeric: oldstyle-nums;
  }
</style>
</head>
<body>
  <main class="canvas">
    <article class="label">
      <header class="brand">
        <span class="brand-name">DORVANE</span>
        <span class="brand-sub">VINEYARDS</span>
      </header>

      <svg class="landscape" role="img" aria-label="Soft watercolour vineyard landscape with rolling hills and dark tree line" viewBox="0 0 720 340" preserveAspectRatio="none">
        <defs>
          <linearGradient id="wash" x1="0" y1="0" x2="0" y2="1">
            <stop offset="0" stop-color="var(--wash-light)" stop-opacity="0"/>
            <stop offset="0.2" stop-color="var(--wash-light)" stop-opacity="0.8"/>
            <stop offset="0.35" stop-color="var(--wash-sand)"/>
            <stop offset="0.48" stop-color="var(--wash-olive)"/>
            <stop offset="0.56" stop-color="var(--wash-moss)"/>
            <stop offset="0.62" stop-color="var(--wash-dark)"/>
            <stop offset="0.7" stop-color="var(--wash-dark)" stop-opacity="0.55"/>
            <stop offset="0.8" stop-color="var(--wash-light)" stop-opacity="0.5"/>
            <stop offset="1" stop-color="var(--wash-light)" stop-opacity="0"/>
          </linearGradient>
        </defs>
        <rect x="0" y="0" width="720" height="340" fill="url(#wash)"/>
      </svg>

      <p class="varietal">PINOD GRIGIO</p>
      <footer class="vintage-band">2014</footer>
    </article>
  </main>
</body>
</html>
```